Jo & Mira's Homepage Design - Florists

Hello PixelHive,

We’re Jo and Mira and we own a lovely flower shop in Marlow. We’re looking to launch a website that gives our customers all information they need to know about getting in contact with us. In time we hope the website will grow and we will want to add new pages as we go along including ecommerce functionality, so the design will need to allow for this.

The brief:
We are looking for 1 homepage design. We have already had our logo designed, which we’ve attached for you to use. At the moment we’re keen to have a homepage design that showcases six of our most popular bouquets, see attached pictures and our contact details. We are looking for a contemporary design that’s inline with our logo. Please do not use dark background colours, we want a clean, light and simple design that looks fresh, modern and professional. Please remember that the majority of web monitors now use a screen resolution of 1366x768. Therefore please do not design a 800 x 600 homepage.

1. Our logo and icon (See attachments)
2. Potential hero images attached for inspiration. 6 Bouquets attached but dont make it look like a bog standard ecommerce site. You dont have to use the 6 bouquets. Our site is more brand as we dont have ecom functionality yet.
3. Our contact details including:

Name:
Jo and Mira’s (note 1 ‘L’ in Mira’s name, use the logo)

Navigation

Homepage needs to include the following copy
‘Free delivery with all orders”
‘Fresh – 7 days of flower freshness guaranteed’
‘Hand delivered and hand prepared by a professional florist’
Very clear call to action to ‘Order today: 0203 554 2071 or email us (visually a clickable link) today

Payment visuals: show that we accept PAYRO/Cardwell/Northern Swift/Quikpay, with logos

Telephone numbers:
0203 554 2071 (Central London)
0208 417 2359 (Greater London)
01628 570213 (Marlow)
07845 190627 (Mobile)

E-mail address
orders@joandmiras.co.uk (Orders)
CS@joandmiras.co.uk (Customer Service)

Chatterly page link (use CH logo)
http://www.facebook.com/joandmiras

The National Petal Guild logo
Attached should be displayed on the bottom of the homepage somewhere, prefer bottom right.

Other sites we like:
http://www.bloomsbyharriet.com
http://maisondepetale.com
Like the fun of this one - http://www.grandpagoose.co.uk/goto/home

Our logo should be a good guide for how we’d like the overall page to look, please use this as a starter for your designs. Fee; free to submit your designs and I’ll feedback on changes.

We look forward to seeing your designs!

Jo & Mira

Industry/Entity Type

Florist

Requirements
Must have
• Please see the attached brief. Please use our logo and icon in the design.
Should not have
• Do not use dark background colours, it should feel light and fresh.

```html
<!DOCTYPE html>
<html lang="en">
<head>
<meta charset="utf-8">
<title>Jo &amp; Mira's – Florists</title>
<link href="https://fonts.googleapis.com/css2?family=Noto+Sans:wght@400;700&family=Arimo:wght@400;700&family=Cormorant+Garamond:ital,wght@1,500&display=swap" rel="stylesheet">
<style>
:root{
  --orange:#e8692a;
  --orange-dark:#c4501a;
  --ink:#222;
  --muted:#555;
  --red:#c0181b;
  --navy:#2c3458;
  --panel:#dfe6ee;
  --panel-edge:#c9d3de;
  --page:#efefef;
  --footer-top:#3a3a3a;
  --footer-bottom:#0c0c0c;
  --gold:#f3a21c;
  --link:#1a3b9a;
}
*{box-sizing:border-box;margin:0;padding:0}
html,body{width:1120px;height:1200px;overflow:hidden}
body{position:relative;background:var(--page);font-family:"Noto Sans",sans-serif;color:var(--ink)}
.abs{position:absolute}
.topbar{left:0;top:0;width:1120px;height:16px;background:#000}
.header-bg{left:0;top:16px;width:1120px;height:102px;background:linear-gradient(#d9d9d9,#f4f4f4);border-bottom:1px solid #fff}
.decor-flower-top{left:808px;top:0;width:208px;height:88px;border-radius:50% 50% 40% 40%;background:radial-gradient(circle at 50% 45%,#ffd21f,#f5b400 55%,rgba(245,180,0,0) 72%)}
.decor-lily{left:0;top:260px;width:220px;height:330px;background:radial-gradient(ellipse at 40% 50%,rgba(255,255,255,.9),rgba(210,215,200,.5) 55%,rgba(239,239,239,0) 75%)}
.decor-flower-left{left:0;top:384px;width:184px;height:112px;background:radial-gradient(ellipse at 50% 50%,#ffcf12,#f2b000 55%,rgba(242,176,0,0) 75%)}
.ribbon-tail{top:98px;width:36px;height:40px;background:var(--orange-dark)}
.ribbon-tail.left{left:142px;clip-path:polygon(0 0,100% 0,100% 100%,20% 100%,40% 50%)}
.ribbon-tail.right{left:942px;clip-path:polygon(0 0,100% 0,60% 50%,80% 100%,0 100%)}
.navband{left:170px;top:88px;width:780px;height:44px;background:linear-gradient(var(--orange),#d85a1e);box-shadow:0 2px 3px rgba(0,0,0,.25)}
.logo{left:178px;top:84px;font-family:"Noto Sans",sans-serif;font-weight:700;font-size:34px;color:#3a3a3a;letter-spacing:-1px}
.logo-dot{left:182px;top:48px;width:22px;height:22px;border-radius:50%;background:var(--orange)}
.nav{left:429px;top:104px;display:flex;gap:0;font-size:11.5px;color:#2a1a10}
.nav a{color:#2a1a10;text-decoration:none;position:absolute;white-space:nowrap}
.main{left:176px;top:132px;width:768px;height:728px;background:#fff;box-shadow:0 0 6px rgba(0,0,0,.08)}
.hero{left:182px;top:142px;width:544px;height:194px;background:#e9eef3;border:2px solid #d5dee8}
.hero-img{position:absolute;top:4px;height:160px}
.hero-caption{position:absolute;left:0;top:160px;width:540px;height:28px;background:rgba(40,40,40,.82);color:#fff;font-weight:700;font-size:16.5px;line-height:28px;padding-left:14px;font-family:"Noto Sans",sans-serif}
.tagline{left:176px;top:346px;width:584px;text-align:center;font-family:"Cormorant Garamond",serif;font-style:italic;font-weight:500;font-size:22px;color:#333}
.card{top:382px;width:165px;height:150px;background:#f1f3f6;border:1px solid #dde;border-radius:4px;box-shadow:0 5px 6px -3px rgba(0,0,0,.35)}
.card.featured{background:var(--navy)}
.card .photo{position:absolute;left:12px;top:7px;width:142px;height:119px;border:1px solid #333}
.card .label{position:absolute;left:18px;top:130px;font-size:10px}
.card .price{position:absolute;right:10px;top:130px;font-size:10px;color:var(--red)}
.card.featured .label,.card.featured .price{color:#ffc400}
.about-h{left:198px;top:551px;font-family:"Cormorant Garamond",serif;font-style:italic;font-size:15px}
.about{left:198px;top:572px;width:517px;font-size:10px;line-height:16px;text-align:justify;color:#222}
.box{width:169px;height:196px;background:linear-gradient(135deg,#e5ebf1,#d6dfe8);border:1px solid var(--panel-edge)}
.box-h{height:22px;background:linear-gradient(90deg,#111 55%,#888 80%,#222);color:#fff;font-family:"Arimo",sans-serif;font-size:13px;line-height:22px;padding-left:11px}
.box ul{list-style:none;padding:10px 0 0 13px}
.box li{font-size:10px;line-height:19.2px;letter-spacing:.3px;color:#222}
.box li::before{content:"-";margin-right:8px}
.delivery{padding:8px 0 0 6px;font-size:9.5px;font-style:italic;line-height:19.2px}
.delivery .sub{font-style:normal;font-size:11px;color:var(--red)}
.delivery a{color:var(--link);font-style:normal;font-size:9.5px}
.side{left:737px;width:199px;background:linear-gradient(135deg,#e7edf3,#d4dde7);border:1px solid var(--panel-edge)}
.side .box-h{height:22px}
.newsletter{top:142px;height:146px}
.newsletter .bar{height:22px;background:linear-gradient(90deg,#111 50%,#999 78%,#222)}
.newsletter label{position:absolute;left:14px;top:34px;font-size:11px}
.newsletter .field{position:absolute;left:9px;top:53px;width:187px;height:20px;background:#fff;border:1px solid #bcc}
.newsletter .ok{position:absolute;left:14px;top:82px;width:45px;height:22px;background:#111;color:#fff;font-weight:700;font-size:12px;text-align:center;line-height:22px;border-radius:4px}
.newsletter .cancel{position:absolute;right:2px;top:87px;font-size:10px;color:#777}
.social{top:296px;height:40px;background:#f3f5f7}
.social span{position:absolute;top:8px;width:23px;height:23px;border-radius:3px}
.latest{top:350px;height:196px}
.latest .item{position:absolute;left:12px}
.latest .thumb{position:absolute;left:0;top:0;width:36px;height:30px;border:2px solid #fff;box-shadow:0 0 3px rgba(0,0,0,.3)}
.latest .t1{position:absolute;left:55px;top:2px;font-size:10px;white-space:nowrap}
.latest .t2{position:absolute;left:55px;top:16px;font-size:10px;color:var(--red);white-space:nowrap}
.favs{top:555px;height:197px}
.badge{left:750px;top:760px;width:160px;height:92px;border-radius:10px;background:linear-gradient(120deg,#f6b135,#f0a020 60%,#2f4a3a)}
.footer{left:0;top:862px;width:1120px;height:140px;background:linear-gradient(var(--footer-top),var(--footer-bottom));border-top:1px solid #777}
.footer h3{position:absolute;font-weight:400;font-size:14px;color:#f47e2e;font-family:"Arimo",sans-serif}
.footer p{position:absolute;font-size:10px;color:#fff;font-family:"Arimo",sans-serif;line-height:17.6px}
.footer .ico{position:absolute;left:0;width:16px;height:16px;border-radius:3px}
.copy{left:0;top:1002px;width:1120px;height:26px;background:#000;color:#fff;font-size:8.5px;text-align:center;line-height:26px;font-family:"Arimo",sans-serif}
</style>
</head>
<body>
<div class="abs topbar"></div>
<div class="abs header-bg"></div>
<div class="abs decor-lily" role="img" aria-label="Soft white lily photograph fading into the page"></div>
<div class="abs decor-flower-top" role="img" aria-label="Yellow flowers photograph"></div>
<div class="abs decor-flower-left" role="img" aria-label="Yellow flowers photograph"></div>

<div class="abs ribbon-tail left"></div>
<div class="abs ribbon-tail right"></div>
<div class="abs navband"></div>
<div class="abs logo-dot"></div>
<div class="abs logo">Jo &amp; Mira's</div>
<nav class="abs nav">
  <a style="left:0">Classic Flowers</a>
  <a style="left:101px">Luxury Bouquets</a>
  <a style="left:211px">Platinum Collection</a>
  <a style="left:333px">Autumn Flowers</a>
  <a style="left:439px">Luxury Roses</a>
</nav>

<div class="abs main"></div>

<section class="abs hero">
  <div class="hero-img" role="img" aria-label="Wrapped bouquet of calla lilies and roses" style="left:4px;width:172px;background:linear-gradient(#c8b59a,#8a6d58 70%,#c6a37c)"></div>
  <div class="hero-img" role="img" aria-label="Bouquet of red and orange roses" style="left:182px;width:172px;background:radial-gradient(circle at 50% 45%,#e23b22,#d6401f 45%,#f4ecea 80%)"></div>
  <div class="hero-img" role="img" aria-label="Heart-shaped floral wreath" style="left:360px;width:172px;background:radial-gradient(circle at 50% 50%,#e8e4dc 18%,#8a9a6a 40%,#b78a90 65%,#e6e2dc)"></div>
  <div class="hero-caption">Hand delivered and hand prepared by a professional florist’</div>
</section>

<div class="abs tagline">Fresh – 7 days of flower freshness Guaranteed’</div>

<div class="abs card featured" style="left:192px">
  <div class="photo" role="img" aria-label="Bright pink and peach bouquet" style="background:radial-gradient(circle at 50% 40%,#f46a7a,#e84a6a 45%,#7a5a3e 85%)"></div>
  <span class="label">We are Young</span><span class="price">£19.99</span>
</div>
<div class="abs card" style="left:373px">
  <div class="photo" role="img" aria-label="Pastel wedding bouquet" style="background:radial-gradient(circle at 50% 45%,#f3d6cf,#c9b2a8 50%,#6f6a56 90%)"></div>
  <span class="label">Wedding flowers</span><span class="price">£24.99</span>
</div>
<div class="abs card" style="left:549px">
  <div class="photo" role="img" aria-label="Autumn arrangement of lilac and green flowers" style="background:radial-gradient(circle at 50% 45%,#b8a6c8,#7c8a62 50%,#4a4a46 90%)"></div>
  <span class="label">Autumn Wonders</span><span class="price">£27.99</span>
</div>

<h2 class="abs about-h">About Us</h2>
<p class="abs about">Welcome to Petalbox, the leading online florist for you to send fresh flowers by post, luxury bouquets, house plants and fun helium balloons from only £11.99 including UK delivery and free milk chocolates.Welcome to Petalbox, the leading online florist for you to send fresh flowers by post, luxury bouquets, house plants and fun helium balloons from only £11.99 including UK delivery and free milk chocolates.</p>

<section class="abs box" style="left:193px;top:652px">
  <div class="box-h">FAQ</div>
  <ul><li>Fertility Diet</li><li>Fertility Cleansing</li><li>Fertility Charting</li><li>Fertility Massage</li><li>Progesterone Fertility Guide</li><li>Estrogen Fertility Guide</li><li>Fertility Massage</li><li>Progesterone Fertility Guide</li></ul>
</section>
<section class="abs box" style="left:374px;top:652px">
  <div class="box-h">Customer Service</div>
  <ul><li>Fertility Diet</li><li>Fertility Cleansing</li><li>Fertility Charting</li><li>Fertility Massage</li><li>Progesterone Fertility Guide</li><li>Estrogen Fertility Guide</li><li>Fertility Massage</li><li>Progesterone Fertility Guide</li></ul>
</section>
<section class="abs box" style="left:554px;top:652px">
  <div class="box-h">Delivery Information</div>
  <div class="delivery">
    <div class="sub">Telephone numbers:</div>
    <div>&nbsp;0203 554 2071 (Central London)</div>
    <div>&nbsp;0208 417 2359 (Greater London)</div>
    <div>&nbsp;01628 570213 (Marlow)</div>
    <div>&nbsp;07845 190627 (Mobile)</div>
    <div class="sub">E-mail address</div>
    <div><a href="#">orders@joandmiras.co.uk (Orders)</a></div>
    <div><a href="#">CS@joandmiras.co.uk</a></div>
  </div>
</section>

<aside class="abs side newsletter">
  <div class="bar"></div>
  <label>Email Address :</label>
  <div class="field"></div>
  <div class="ok">OK</div>
  <span class="cancel">Cancel</span>
</aside>
<div class="abs side social">
  <span style="left:17px;background:#f08a1c"></span>
  <span style="left:45px;background:#3aa5dc"></span>
  <span style="left:73px;background:#3b5998"></span>
  <span style="left:101px;background:#1d7bb8"></span>
  <span style="left:129px;background:#6d8fc8"></span>
  <span style="left:157px;background:#e0e0e0"></span>
</div>
<aside class="abs side latest">
  <div class="box-h">Latest Designs</div>
  <div class="item" style="top:30px"><div class="thumb" role="img" aria-label="Bouquet thumbnail" style="background:#8a9476"></div><span class="t1">Leaflab Studio</span><span class="t2">magazine theme</span></div>
  <div class="item" style="top:72px"><div class="thumb" role="img" aria-label="Bouquet thumbnail" style="background:#c6b7ac"></div><span class="t1">Leaflab Studio</span><span class="t2">magazine theme</span></div>
  <div class="item" style="top:114px"><div class="thumb" role="img" aria-label="Bouquet thumbnail" style="background:#e06a78"></div><span class="t1">Leaflab Studio</span><span class="t2">magazine theme</span></div>
</aside>
<aside class="abs side box favs" style="width:199px">
  <div class="box-h">Our Favourites</div>
  <ul><li>Fertility Diet</li><li>Fertility Cleansing</li><li>Fertility Charting</li><li>Fertility Massage</li><li>Progesterone Fertility Guide</li><li>Estrogen Fertility Guide</li><li>Fertility Massage</li><li>Progesterone Fertility Guide</li></ul>
</aside>
<div class="abs badge" role="img" aria-label="The National Petal Guild membership badge"></div>

<footer class="abs footer">
  <h3 style="left:214px;top:22px">Recent Blogs</h3>
  <p style="left:214px;top:45px">Varius dui, quis posuere nibh huj<br>Mollisuis. Mauris omma rhoncus<br>Porttitor. http://quillthemes.com<br>Varius dui, quis posuere nibh huj</p>
  <h3 style="left:782px;top:22px">Keep in touch</h3>
  <div class="abs" style="left:783px;top:45px;width:200px;height:90px">
    <span class="ico" style="top:2px;background:#ddd"></span>
    <span class="ico" style="top:24px;background:#1d7bb8"></span>
    <span class="ico" style="top:46px;background:#f08a1c"></span>
    <span class="ico" style="top:68px;background:#3aa5dc"></span>
    <p style="left:23px;top:0;line-height:22.4px">Connect via Introly<br>Connect via Linkline<br>Subscribe to our blog<br>Follow on Chirper</p>
  </div>
</footer>
<div class="abs copy">2011 © Quill. All rights reserved</div>
</body>
</html>
```